Four Oaks Haulage Website (quoting web application)

We need a website designed for our furniture moving company in Cape Town, South Africa.

I have attached some logos and images for you to use.

I have also attached the layout of the three pages we want designed (pdf file)

Dark blue is our colour.

The pictures of our trucks (uploaded) epitomise the design required.

Our old site (existing) is viewable here: fouroakshaulage.co.za

Target Market(s)

People moving house in Cape Town, South Africa.

Number of Pages Required

3 page

Font styles to use
Sans Serif

Colors
0255a3

Requirements
Must have
• Page design for the 3 pages in the pdf file.

```html
<!DOCTYPE html>
<html lang="en">
<head>
<meta charset="utf-8">
<title>Four Oaks Haulage – Furniture Removals Cape Town</title>
<link href="https://fonts.googleapis.com/css2?family=Raleway:wght@400;500;600;700&family=Lato:wght@400;700&display=swap" rel="stylesheet">
<style>
:root{
  --navy:#0b3a73;
  --navy-deep:#08305f;
  --brand:#0255a3;
  --accent:#5d80d3;
  --soft-btn:#8ea2d6;
  --ink:#1c1c1c;
  --body:#3a3a3a;
  --muted:#8a8a8a;
  --line:#e2e2e2;
  --footer:#2f2f2f;
  --footer-bar:#222;
  --white:#fff;
}
*{box-sizing:border-box;margin:0;padding:0}
html,body{width:1200px;height:3896px;overflow:hidden;background:var(--white)}
body{font-family:"Lato",sans-serif;color:var(--body);position:relative}
section,header,nav,footer{position:relative;width:1200px;overflow:hidden}
.abs{position:absolute}
h1,h2,h3{font-family:"Raleway",sans-serif;font-weight:500;color:var(--ink)}

/* header */
.site-header{height:109px}
.brand{left:143px;top:30px;display:flex;align-items:center;gap:12px;font-family:"Raleway",sans-serif;font-weight:700;font-size:22px;color:var(--navy)}
.brand-square{width:40px;height:40px;background:var(--navy)}
.social-top{right:47px;top:39px;display:flex;gap:8px}
.social-dot{width:32px;height:32px;border-radius:50%;border:2px solid var(--navy)}

/* nav */
.main-nav{height:47px;background:var(--navy)}
.main-nav ul{list-style:none}
.main-nav li{position:absolute;top:15px;color:var(--white);font-size:14px;letter-spacing:.3px;font-family:"Raleway",sans-serif;font-weight:500}

/* hero */
.hero{height:449px}
.hero-photo{inset:0;background:linear-gradient(100deg,#cfd3d8 0%,#8b96a3 30%,#2a4f94 55%,#1f4a9a 75%,#d9d6cf 100%)}
.hero-panel{left:104px;top:182px;width:540px;height:234px;background:rgba(255,255,255,.88);padding:34px 36px}
.hero-panel h1{font-size:34px;line-height:42px;font-weight:500;color:#2a2a2a}
.hero-panel h1 em{font-style:normal;color:var(--accent)}
.hero-panel p{margin-top:12px;font-size:15px;line-height:21px;color:#333}
.hero-next{left:644px;top:364px;width:70px;height:52px;background:var(--navy-deep);display:flex;align-items:center;justify-content:center}

/* intro */
.intro{height:231px;text-align:center}
.intro h2{position:absolute;top:72px;width:100%;font-size:33px}
.intro p{position:absolute;top:124px;left:300px;width:600px;font-size:14px;line-height:22px;color:#555}

/* covered */
.covered{height:385px}
.covered-photo{left:104px;top:0;width:473px;height:317px;background:linear-gradient(135deg,#e9e9ea,#c7cbd2 55%,#3f5677)}
.covered-text{left:670px;top:6px;width:430px}
.covered-text h2{font-size:38px;font-weight:700;color:#111;margin-bottom:18px}
.covered-text p{font-size:14.5px;line-height:24px;color:#333;margin-bottom:8px}
.btn-soft{display:inline-block;background:var(--soft-btn);color:var(--white);font-size:16px;font-family:"Raleway",sans-serif;padding:14px 22px}
.covered .btn-soft{position:absolute;left:670px;top:257px;width:230px;height:48px;text-align:center;padding:14px 0}

/* features */
.features{height:553px;background:var(--navy)}
.features h2{position:absolute;top:52px;width:100%;text-align:center;color:var(--white);font-size:33px;font-weight:400}
.feature{position:absolute;width:290px;text-align:center;color:var(--white)}
.feature svg{display:block;margin:0 auto 14px}
.feature h3{color:#cfe0ff;font-family:"Lato",sans-serif;font-weight:700;font-size:15px;letter-spacing:.6px;margin-bottom:10px}
.feature p{font-size:14px;line-height:22px;color:#eef2fa}

/* why */
.why{height:841px;border-bottom:1px solid var(--line)}
.why h2{position:absolute;top:64px;width:100%;text-align:center;font-size:33px}
.why-lead{position:absolute;top:136px;left:270px;width:660px;text-align:center;font-size:14px;line-height:22px;color:#555}
.work{position:absolute;top:228px;width:480px}
.work-photo{width:480px;height:320px}
.work h3{margin-top:48px;font-family:"Lato",sans-serif;font-weight:700;font-size:17px;letter-spacing:.4px;color:#222}
.work p{margin-top:12px;font-size:14px;line-height:22px;color:#444;width:420px}
.play{left:204px;top:130px}
.why .btn-soft{position:absolute;left:493px;top:737px;width:213px;height:47px;border-radius:24px;text-align:center;padding:14px 0;font-weight:600}

/* customers */
.customers{height:615px}
.customers h2{position:absolute;top:56px;width:100%;text-align:center;font-size:33px}
.review-card{position:absolute;top:133px;width:274px;height:454px;background:var(--white);box-shadow:0 1px 6px rgba(0,0,0,.18)}
.review-photo{height:218px}
.tweet{margin:12px 10px;border:1px solid var(--line);border-radius:4px;padding:8px 10px;font-size:10px;line-height:14px;color:#444}
.tweet-quote{border-left:2px solid var(--line);padding-left:8px;margin-bottom:10px;color:#555}
.tweet-author{display:flex;align-items:center;gap:6px;margin-bottom:6px}
.avatar{width:20px;height:20px;border-radius:50%;background:#9aa4b1}
.tweet-author b{font-size:10.5px;color:#222;display:block}
.tweet-author span{color:var(--muted)}
.tweet a{color:var(--brand);text-decoration:none}
.tweet-meta{color:var(--muted);margin-top:6px}
.tweet-foot{color:var(--muted);margin-top:6px;border-top:1px solid var(--line);padding-top:6px}

/* about */
.about{height:336px;text-align:center}
.about h2{position:absolute;top:10px;width:100%;font-size:36px}
.about-rule{left:540px;top:72px;width:120px;height:1px;background:#666}
.about p{position:absolute;left:150px;width:900px;font-size:14px;line-height:24px;color:#444}

/* footer */
.site-footer{height:278px;background:var(--footer);color:#ddd}
.footer-brand{left:150px;top:80px;display:flex;align-items:center;gap:10px;font-family:"Raleway",sans-serif;font-weight:700;font-size:18px;color:#cfcfcf}
.footer-brand .brand-square{width:30px;height:30px;background:#cfcfcf}
.footer-col{top:78px}
.footer-col h4{font-family:"Lato",sans-serif;font-weight:700;font-size:14px;letter-spacing:.6px;color:var(--white);padding-bottom:10px;border-bottom:1px solid #777;width:140px;margin-bottom:10px}
.footer-col ul{list-style:none;font-size:12px;line-height:21px;color:#e8e8e8}
.footer-social{display:flex;gap:8px;margin-top:6px}
.footer-social .social-dot{width:28px;height:28px;border-color:#ddd}
.copyright{height:52px;background:var(--footer-bar);color:#ddd;text-align:center;font-size:14px;line-height:52px}
</style>
</head>
<body>

<header class="site-header">
  <div class="abs brand"><span class="brand-square"></span>Four Oaks Haulage</div>
  <div class="abs social-top" aria-label="Social links">
    <span class="social-dot"></span><span class="social-dot"></span><span class="social-dot"></span><span class="social-dot"></span>
  </div>
</header>

<nav class="main-nav">
  <ul>
    <li style="left:130px">HOME</li>
    <li style="left:197px">SERVICES</li>
    <li style="left:301px">WHY CHOOSE US</li>
    <li style="left:442px">ARTICLES</li>
    <li style="left:553px">CONTACT US</li>
    <li style="left:680px">INSTANT QUOTE</li>
  </ul>
</nav>

<section class="hero">
  <div class="abs hero-photo" role="img" aria-label="Moving crew in uniform standing in front of a blue removal truck"></div>
  <div class="abs hero-panel">
    <h1>We are a company that specialises in <em>leadership learning</em></h1>
    <p>Our products include leadership programme development, consulting and guest speaking.</p>
  </div>
  <div class="abs hero-next">
    <svg width="14" height="18" viewBox="0 0 14 18"><path d="M3 2l8 7-8 7" fill="none" stroke="#fff" stroke-width="3"/></svg>
  </div>
</section>

<section class="intro">
  <h2>Furniture Removals Cape Town</h2>
  <p>With our furniture removal company your move is insured. Obtaining a quote and booking your move with our Cape Town movers is as quick and easy as possible.</p>
</section>

<section class="covered">
  <div class="abs covered-photo" role="img" aria-label="Two movers in caps carrying goods through a doorway"></div>
  <div class="abs covered-text">
    <h2>We’ve got you covered</h2>
    <p>When our Cape Town furniture removal team do your move we provide all risk goods in transit insurance, free of charge, on goods up to a value of R100 000.</p>
    <p>This means that in the unlikely event that your furniture is damaged, we will replace or repair it. Please note that standard insurance excesses and terms apply.</p>
  </div>
  <a class="btn-soft">Get and Instant Quote</a>
</section>

<section class="features">
  <h2>Popular features that will change your life</h2>

  <div class="feature" style="left:154px;top:164px">
    <svg width="44" height="44" viewBox="0 0 44 44" fill="none" stroke="#fff" stroke-width="2"><path d="M22 4l14 6v10c0 10-6 17-14 20C14 37 8 30 8 20V10z"/><path d="M26 15c-1-2-3-2-4-2-3 0-4 2-4 3 0 5 8 3 8 7 0 2-2 3-4 3s-4-1-4-3M22 11v2M22 26v3"/></svg>
    <h3>FULLY INSURED</h3>
    <p>We will fix or replace any furniture damaged during your Cape Town furniture removal.</p>
  </div>
  <div class="feature" style="left:458px;top:164px">
    <svg width="44" height="44" viewBox="0 0 44 44" fill="none" stroke="#fff" stroke-width="2"><path d="M22 20c-4-3-9-6-9-10 0-3 4-5 9 0 5-5 9-3 9 0 0 4-5 7-9 10z" fill="#fff"/><path d="M4 30h8l6 4h10c2 0 2-3 0-3h-8M12 38h18l10-8c1-1 0-3-2-2l-8 4"/></svg>
    <h3>SPECIAL SERVICES</h3>
    <p>We have a range of special services to make your move go smoothly.</p>
  </div>
  <div class="feature" style="left:762px;top:164px">
    <svg width="44" height="44" viewBox="0 0 44 44" fill="none" stroke="#fff" stroke-width="2"><path d="M22 40s-12-12-12-22a12 12 0 0124 0c0 10-12 22-12 22z"/><circle cx="22" cy="18" r="5"/></svg>
    <h3>WE ARRIVE ON TIME</h3>
    <p>We arrive for your Cape Town move on time.</p>
  </div>
  <div class="feature" style="left:154px;top:350px">
    <svg width="44" height="44" viewBox="0 0 44 44" fill="none" stroke="#fff" stroke-width="2"><path d="M3 18l8-6 7 3 8-3 6 2 9 4M11 12l-6 14M33 14l6 12M14 26l6 6c1 1 3 1 4 0l8-8-8-7-6 3"/></svg>
    <h3>PROFESSIONAL &amp; FRIENDLY</h3>
    <p>We take pride in our service and ensure a smooth and hassle-free move with our friendly movers.</p>
  </div>
  <div class="feature" style="left:458px;top:350px">
    <svg width="44" height="44" viewBox="0 0 44 44" fill="none" stroke="#fff" stroke-width="2"><circle cx="22" cy="14" r="5"/><circle cx="10" cy="20" r="4"/><circle cx="34" cy="20" r="4"/><path d="M13 36c0-6 4-10 9-10s9 4 9 10M3 36c0-5 3-8 7-8M41 36c0-5-3-8-7-8"/></svg>
    <h3>TRAINED EXPERTS</h3>
    <p>We have been doing your moves in Cape Town for more than 4 years.</p>
  </div>
  <div class="feature" style="left:762px;top:350px">
    <svg width="44" height="44" viewBox="0 0 44 44" fill="none" stroke="#fff" stroke-width="2"><circle cx="22" cy="22" r="17"/><circle cx="16" cy="18" r="1.5" fill="#fff"/><circle cx="28" cy="18" r="1.5" fill="#fff"/><path d="M14 26c4 5 12 5 16 0"/></svg>
    <h3>HAPPY CUSTOMERS</h3>
    <p>Read what our happy customers say about our Cape Town removals.</p>
  </div>
</section>

<section class="why">
  <h2>Why choose us?</h2>
  <p class="why-lead">We are a professional furniture moving company offering home moves, office moves, mini moves and storage. If you need expert furniture removal in Cape Town, we are your men!</p>

  <article class="work" style="left:104px">
    <div class="work-photo" role="img" aria-label="Movers wrapping a sofa on a lawn" style="background:linear-gradient(160deg,#6f8a4f,#4e6b38 60%,#3d4a3a)"></div>
    <svg class="abs play" width="46" height="46" viewBox="0 0 46 46"><circle cx="23" cy="23" r="23" fill="#1f2a36"/><path d="M18 14l14 9-14 9z" fill="#fff"/></svg>
    <h3>PEOPLE OF CAPE TOWN LOVE US</h3>
    <p>“Just want to say thanks for great service. U have a superb team who work well together. Tell the Men I say thank you and well done!”</p>
  </article>
  <article class="work" style="left:621px">
    <div class="work-photo" role="img" aria-label="Removal truck parked on a colourful Cape Town street" style="background:linear-gradient(180deg,#b9d0ea,#3e8ad6 40%,#5a5e66 70%,#8c8f94)"></div>
    <h3>PEOPLE OF CAPE TOWN LOVE US</h3>
    <p>“Just want to say thanks for great service. U have a superb team who work well together. Tell the Men I say thank you and well done!”</p>
  </article>

  <a class="btn-soft">See More Works</a>
</section>

<section class="customers">
  <h2>Customer Says</h2>

  <article class="review-card" style="left:169px">
    <div class="review-photo" role="img" aria-label="Movers loading a wardrobe into a truck" style="background:linear-gradient(135deg,#3b3b3d,#6a6560 60%,#2c2c2e)"></div>
    <div class="tweet">
      <div class="tweet-quote">@lindiwe_m · Jul 19, 2016<br>Hey @capehelpdesk – recommendations for a moving company to move a flat from @mothercityinfo CBD to Woodstock, please? @capehelpdesk</div>
      <div class="tweet-author"><span class="avatar"></span><div><b>Dan Ferreira</b><span>@DanFerreiraCook</span></div></div>
      I used “Four Oaks Haulage” last week and they were excellent <a>fouroakshaulage.co.za</a>
      <div class="tweet-meta">12:56 AM · Jun 20, 2016</div>
      <div class="tweet-foot">♡ 1 · See Dan Ferreira’s other Tweets</div>
    </div>
  </article>
  <article class="review-card" style="left:478px">
    <div class="review-photo" role="img" aria-label="Inside of an empty truck with chairs being loaded" style="background:linear-gradient(180deg,#f1f0ec,#d8d5cf 60%,#7e7a74)"></div>
    <div class="tweet">
      <div class="tweet-quote">@lindiwe_m · Jul 19, 2016<br>Hey @capehelpdesk – recommendations for a moving company to move a flat from @mothercityinfo CBD to Woodstock, please? @capehelpdesk</div>
      <div class="tweet-author"><span class="avatar"></span><div><b>Dan Ferreira</b><span>@DanFerreiraCook</span></div></div>
      I used “Four Oaks Haulage” last week and they were excellent <a>fouroakshaulage.co.za</a>
      <div class="tweet-meta">12:56 AM · Jun 20, 2016</div>
      <div class="tweet-foot">♡ 1 · See Dan Ferreira’s other Tweets</div>
    </div>
  </article>
  <article class="review-card" style="left:787px">
    <div class="review-photo" role="img" aria-label="Mover in uniform carrying household items" style="background:linear-gradient(135deg,#e6e2da,#9d8f7b 55%,#2f3b5a)"></div>
    <div class="tweet">
      <div class="tweet-quote">@lindiwe_m · Jul 19, 2016<br>Hey @capehelpdesk – recommendations for a moving company to move a flat from @mothercityinfo CBD to Woodstock, please? @capehelpdesk</div>
      <div class="tweet-author"><span class="avatar"></span><div><b>Dan Ferreira</b><span>@DanFerreiraCook</span></div></div>
      I used “Four Oaks Haulage” last week and they were excellent <a>fouroakshaulage.co.za</a>
      <div class="tweet-meta">12:56 AM · Jun 20, 2016</div>
      <div class="tweet-foot">♡ 1 · See Dan Ferreira’s other Tweets</div>
    </div>
  </article>
</section>

<section class="about">
  <h2>About us</h2>
  <div class="abs about-rule"></div>
  <p style="top:96px">Punctuality. Honesty. Care.</p>
  <p style="top:148px">We are a Cape Town furniture removal company with offices in Woodstock who do furniture removals for Cape Town. We have been Cape Town movers since 2012 so if you need furniture removal done well in Cape Town we are your men.</p>
  <p style="top:216px">We have large trucks for big removals but we also have smaller fuel efficient vehicles which make your mini moves quick and affordable.</p>
  <p style="top:266px">We are experienced, trained removal experts who know how to deal with all of your moving situations.</p>
</section>

<footer class="site-footer">
  <div class="abs footer-brand"><span class="brand-square"></span>Four Oaks Haulage</div>
  <div class="abs footer-col" style="left:429px">
    <h4>GROUP BUSINESSES</h4>
    <ul><li>HOME</li><li>SERVICES</li><li>WHY CHOOSE US</li><li>ARTICLES</li><li>CONTACT US</li><li>INSTANT QUOTE</li></ul>
  </div>
  <div class="abs footer-col" style="left:761px">
    <h4 style="border:none;width:auto">GET CONNECT WITH &nbsp;US</h4>
    <div class="footer-social"><span class="social-dot"></span><span class="social-dot"></span><span class="social-dot"></span><span class="social-dot"></span></div>
  </div>
</footer>
<div class="copyright">© 2018 All Right Reserved</div>

</body>
</html>
```